Website for Sports and Exercise Medicine Doctor with active research in stem cells therapies.

I am a sports and exercise medicine doctor with research interests in the cutting edge areas of biological therapies, most notable stem cells. None of my patients are dying of anything, and most of them come to see me to decrease their pain, so they can get back to what they want to do.

The approach i then take is to decrease their pain and support them to achieve the things they wish to achieve. Most people start at "Just make it stop hurting doc" , but I try to move them towards something more important over time.

I would like the website to be very different to other "Doctor or medical websites" in its look. No pictures of doctors in white coats and no pictures of fit old people smiling. I would potentially like the fist thing seen to be a quote:

"Less pain. Everybody wants it, but what are you going to do, once you've got it?"

(But this is only an idea, I am open to anything)

The website will need a couple of things

1. "Locations" I work
2. "Research" I am involved in
3. "Sort Me out" - Clinical information for people to access
4. "Social" - imbedded twitter and facebook
5. "Blog" - imbedded wordpress blog
6. "Bio" - the usual bio-stuff

The "Sort Me out" - pages I would like to have the functionality as seen in this site http://www.veltarion.com.au/platelet/. I intend to put disease topics into these pages (eg Achilles tehdinopathy, osteoarthritis etc etc etc). Once again I am not wedded to this but something along these lines would be good.

To give you an idea these are some sites I like
http://www.morbanquilt.com/
http://daptrine.com/
http://ovimbera.com.sg/
http://jolvaniketchup.com/
http://www.pilnorwave.com/
http://quadrisel.com/#offering
http://fennikstudio.tv/
http://norvalgate.com/
http://sablethorn.co.uk/#about

Target Market(s)

20-80 year old.
People with tendon injuries
People with osteoarthritis
People interested in stem cells
I will build the site over time to contain information on multiple sporting injuries and musculoskeletal disorders. It will also become a site for the latest on stem cell research particularly in the area of osteoarthritis.

Industry/Entity Type

Medical

Font styles to use
Sans Serif

Colors
ffffff

Requirements
Nice to have
• To give you an idea these are some sites I like
http://daptrine.com/
http://fennikstudio.tv/
http://norvalgate.com/
Should not have
• Pictures of doctors in white coats or old fit people smiling

```html
<!DOCTYPE html>
<html lang="en">
<head>
<meta charset="utf-8">
<title>kelvo — Sports &amp; Exercise Medicine</title>
<link rel="stylesheet" href="https://fonts.googleapis.com/css2?family=Lato:wght@300;400&family=Questrial&display=swap">
<style>
  :root {
    --teal: #36778b;
    --teal-dark: #2f6b7e;
    --ink: #2b2b2b;
    --body-text: #474747;
    --panel: #f2f2f2;
    --card: #fdfdfd;
    --card-line: #e6e6e6;
    --footer: #3e3d43;
    --search: #6b6b6b;
    --white: #ffffff;
    --black: #0b0b0b;
  }
  * { box-sizing: border-box; margin: 0; padding: 0; }
  html, body { width: 1200px; height: 1188px; overflow: hidden; background: var(--white); }
  body { position: relative; font-family: "Lato", sans-serif; color: var(--ink); }

  .site-header { position: absolute; left: 0; top: 0; width: 1200px; height: 127px; }
  .brand { position: absolute; left: 117px; top: 34px; font-family: "Lato", sans-serif; font-weight: 300; font-size: 60px; line-height: 80px; color: var(--teal); letter-spacing: 1px; }
  .search { position: absolute; left: 907px; top: 20px; width: 180px; height: 26px; background: var(--search); display: flex; }
  .search-field { flex: 1; font-size: 14px; color: #f0f0f0; line-height: 26px; padding-left: 10px; }
  .search-button { width: 22px; margin: 2px; background: var(--teal); display: flex; align-items: center; justify-content: center; }
  .main-nav { position: absolute; top: 78px; left: 0; }
  .main-nav a { position: absolute; top: 0; font-size: 12px; letter-spacing: 1.6px; color: var(--ink); text-decoration: none; white-space: nowrap; line-height: 14px; }
  .nav-active-bar { position: absolute; left: 372px; top: 121px; width: 47px; height: 6px; background: var(--teal); }

  .hero { position: absolute; left: 11px; top: 127px; width: 1178px; height: 503px; overflow: hidden; }
  .hero-photo { position: absolute; inset: 0;
    background:
      radial-gradient(ellipse 200px 200px at 745px 170px, #b8956a 0%, rgba(184,149,106,0) 70%),
      radial-gradient(ellipse 300px 200px at 1050px 320px, #2b6a3a 0%, rgba(43,106,58,0) 70%),
      radial-gradient(ellipse 260px 260px at 330px 120px, #3a2e2a 0%, rgba(58,46,42,0) 70%),
      linear-gradient(180deg, #b5b29a 0%, #a9a78c 45%, #6e7440 75%, #3f4a22 100%); }
  .hero-slogan { position: absolute; left: 0; width: 100%; top: 213px; text-align: center; font-weight: 300; font-size: 43px; color: var(--white); letter-spacing: 0.5px; line-height: 52px; }
  .hero-sub { position: absolute; left: 411px; top: 272px; width: 397px; height: 24px; background: var(--teal); color: var(--white); font-size: 18px; line-height: 24px; text-align: center; }
  .hero-cta { position: absolute; left: 531px; top: 320px; width: 138px; height: 30px; background: var(--black); color: var(--white); font-family: "Questrial", sans-serif; font-size: 18px; line-height: 30px; text-align: center; }
  .slider-arrow { position: absolute; top: 216px; width: 33px; height: 72px; background: var(--black); display: flex; align-items: center; justify-content: center; }
  .slider-arrow.prev { left: 0; }
  .slider-arrow.next { right: 0; }

  .services { position: absolute; left: 11px; top: 630px; width: 1178px; height: 359px; background: var(--panel); }
  .service-card { position: absolute; top: 35px; width: 312px; height: 288px; background: var(--card); border: 1px solid var(--card-line); text-align: center; }
  .service-icon { position: absolute; left: 0; top: 55px; width: 100%; height: 64px; display: flex; justify-content: center; }
  .service-title { position: absolute; top: 145px; width: 100%; font-size: 22px; font-weight: 400; color: var(--teal); line-height: 26px; }
  .service-text { position: absolute; top: 198px; width: 100%; font-size: 16px; font-weight: 300; color: var(--body-text); line-height: 19.5px; }

  .site-footer { position: absolute; left: 11px; top: 989px; width: 1178px; height: 152px; background: var(--footer); }
  .footer-brand { position: absolute; left: 0; width: 100%; top: 12px; text-align: center; font-weight: 300; font-size: 60px; line-height: 80px; color: var(--white); letter-spacing: 1px; }
  .social-links { position: absolute; top: 111px; left: 508px; }
  .social-links span { position: absolute; top: 0; width: 30px; height: 30px; background: var(--black); }
  .legal-bar { position: absolute; left: 11px; top: 1141px; width: 1178px; height: 32px; background: var(--teal); color: var(--white); font-family: "Questrial", sans-serif; font-size: 11px; line-height: 32px; }
  .legal-bar .copyright { position: absolute; left: 113px; }
  .legal-bar .phone { position: absolute; left: 775px; }
  .legal-bar .email { position: absolute; left: 925px; }
  .legal-bar .email a { color: #d8e6ea; text-decoration: underline; }
</style>
</head>
<body>
  <header class="site-header">
    <div class="brand">kelvo</div>
    <div class="search">
      <span class="search-field">Search Me</span>
      <span class="search-button">
        <svg width="10" height="10" viewBox="0 0 10 10"><circle cx="4" cy="4" r="2.8" fill="none" stroke="#fff" stroke-width="1.6"/><line x1="6" y1="6" x2="9" y2="9" stroke="#fff" stroke-width="1.8"/></svg>
      </span>
    </div>
    <nav class="main-nav">
      <a style="left:375px">HOME</a>
      <a style="left:474px">ABOUT US</a>
      <a style="left:584px">RESEARCH</a>
      <a style="left:702px">SORT ME OUT</a>
      <a style="left:839px">BIO</a>
      <a style="left:912px">LOCATION</a>
      <a style="left:1026px">BLOG</a>
    </nav>
    <div class="nav-active-bar"></div>
  </header>

  <section class="hero">
    <div class="hero-photo" role="img" aria-label="Action photo of a football match: a player kicking the ball past a diving goalkeeper with mud splashing on the pitch"></div>
    <h1 class="hero-slogan">LESS PAIN, EVERYBODY WANTS IT.</h1>
    <p class="hero-sub">But what are you going to do, once you've got it?</p>
    <div class="hero-cta">read more</div>
    <div class="slider-arrow prev"><svg width="12" height="22" viewBox="0 0 12 22"><polyline points="11,1 1,11 11,21" fill="none" stroke="#fff" stroke-width="1.5"/></svg></div>
    <div class="slider-arrow next"><svg width="12" height="22" viewBox="0 0 12 22"><polyline points="1,1 11,11 1,21" fill="none" stroke="#fff" stroke-width="1.5"/></svg></div>
  </section>

  <section class="services">
    <article class="service-card" style="left:99px">
      <div class="service-icon">
        <svg width="50" height="64" viewBox="0 0 50 64" fill="#333">
          <rect x="20" y="2" width="8" height="6" transform="rotate(25 24 5)"/>
          <rect x="16" y="8" width="10" height="26" rx="2" transform="rotate(25 21 21)"/>
          <path d="M28 26a12 12 0 0 1 0 24h-6v-4h6a8 8 0 0 0 0-16z"/>
          <rect x="10" y="32" width="16" height="5"/>
          <rect x="4" y="52" width="42" height="6"/>
          <rect x="12" y="46" width="20" height="6"/>
        </svg>
      </div>
      <h2 class="service-title">RESEARCH</h2>
      <p class="service-text">Lorem ipsum dolor a sit eget amet,<br>consectetur adipiscing elit in sit amet<br>aliquet odio, nec vehicula leo.</p>
    </article>
    <article class="service-card" style="left:434px">
      <div class="service-icon">
        <svg width="58" height="64" viewBox="0 0 58 64">
          <path d="M21 14v-4h16v4" fill="none" stroke="#333" stroke-width="3"/>
          <rect x="2" y="14" width="54" height="38" rx="3" fill="#333"/>
          <line x1="2" y1="30" x2="56" y2="30" stroke="#fdfdfd" stroke-width="2"/>
          <rect x="23" y="25" width="12" height="12" rx="2" fill="#333" stroke="#fdfdfd" stroke-width="2"/>
        </svg>
      </div>
      <h2 class="service-title">SORT ME OUT</h2>
      <p class="service-text">Lorem ipsum dolor a sit eget amet,<br>consectetur adipiscing elit in sit amet<br>aliquet odio, nec vehicula leo.</p>
    </article>
    <article class="service-card" style="left:764px">
      <div class="service-icon">
        <svg width="52" height="64" viewBox="0 0 52 64">
          <rect x="4" y="5" width="36" height="52" rx="3" fill="none" stroke="#333" stroke-width="3"/>
          <line x1="11" y1="18" x2="33" y2="18" stroke="#333" stroke-width="2.5"/>
          <line x1="11" y1="26" x2="33" y2="26" stroke="#333" stroke-width="2.5"/>
          <line x1="11" y1="34" x2="26" y2="34" stroke="#333" stroke-width="2.5"/>
          <path d="M24 52l4-10 18-18 6 6-18 18z" fill="#333"/>
        </svg>
      </div>
      <h2 class="service-title">BIO</h2>
      <p class="service-text">Lorem ipsum dolor a sit eget amet,<br>consectetur adipiscing elit in sit amet<br>aliquet odio, nec vehicula leo.</p>
    </article>
  </section>

  <footer class="site-footer">
    <div class="footer-brand">kelvo</div>
    <div class="social-links">
      <span style="left:0"></span>
      <span style="left:53px"></span>
      <span style="left:108px"></span>
    </div>
  </footer>
  <div class="legal-bar">
    <span class="copyright">Copyright 2013 - ravenmed.com - All Rights Reserved</span>
    <span class="phone">Phone: +38 045 712-30-96</span>
    <span class="email">E-mail: <a>support@ravenmed.com</a></span>
  </div>
</body>
</html>
```